EPIC, awesome, creative business card needed - get involved!

I'm launching a boutique, exclusive Property Management real estate agency in Sydney early next year.
The name of the agency will be called "Quartz Hill Lane" - it's a play on "chase the silver pebble trail" to wealth. The Quartz Hill Lane signifies wealth through property investment.
My business will offer management of investment properties (ie Property Management).
The difference with Quartz Hill Lane and other agencies is the business will be run by one of Australia's leading property investment experts, and also one of Australia's leading property managers.
It will be exclusively for high net worth properties and individuals, so the business card needs to be extremely sharp, slick and relatively simple.
The information I want on the card is as follows
Nolan Pryce - Director
M: 0412 967 154
P: 9735 6021
E: nolan@quartzhilllane.net.au
W: quartzhilllane.net.au
I'm happy with the red from the logo, black - no yellows or funky colors. I want this to be a super corporate and slick business card to match the high end nature of the business.
Good luck everyone, and please ask questions for clarification.

```html
<!DOCTYPE html>
<html lang="en">
<head>
<meta charset="utf-8">
<title>Quartz Hill Lane – Business Card</title>
<link rel="stylesheet" href="https://fonts.googleapis.com/css2?family=Montserrat:wght@400;500;700&display=swap">
<style>
  :root {
    --stage: #e7e5e2;
    --card-white: #f8f7f4;
    --card-black: #141414;
    --brand-red: #d2202a;
    --ink: #2b2b2b;
    --ink-soft: #7a7a7a;
    --paper-white: #ffffff;
    --card-shadow: 0 14px 34px rgba(0,0,0,0.18);
  }
  * { box-sizing: border-box; margin: 0; padding: 0; }
  html, body {
    width: 1200px; height: 1000px; overflow: hidden;
    background: var(--stage);
    font-family: "Montserrat", Arial, sans-serif;
  }
  .sheet {
    width: 1200px; height: 1000px;
    display: flex; flex-direction: column;
    align-items: center; justify-content: center; gap: 60px;
  }
  .card {
    width: 780px; height: 420px;
    border-radius: 34px;
    box-shadow: var(--card-shadow);
    position: relative;
  }
  .card--front { background: var(--card-white); }
  .card--back { background: var(--card-black); }

  .brand {
    position: absolute;
    display: flex; align-items: center; gap: 14px;
  }
  .brand__square {
    width: 46px; height: 46px; background: var(--brand-red); flex: none;
  }
  .brand__name {
    font-weight: 700; font-size: 30px; line-height: 1.05;
    text-transform: uppercase; letter-spacing: 1px;
    color: var(--brand-red);
    width: 170px;
  }
  .card--front .brand { left: 70px; top: 150px; }
  .card--back .brand { left: 410px; top: 140px; }
  .card--back .brand__name { color: var(--paper-white); }

  .tagline {
    position: absolute; left: 470px; top: 262px;
    color: var(--paper-white); font-size: 17px; font-weight: 400;
  }

  .contact {
    position: absolute; left: 400px; top: 110px;
    color: var(--ink);
  }
  .contact__name { font-size: 22px; font-weight: 500; }
  .contact__role { font-size: 12px; color: var(--ink-soft); margin-bottom: 22px; }
  .contact__list { list-style: none; }
  .contact__item {
    display: flex; align-items: center; gap: 10px;
    font-size: 18px; line-height: 27px;
  }
  .contact__icon { width: 16px; height: 16px; flex: none; fill: var(--ink); }
  .contact__label { width: 16px; font-weight: 700; font-size: 15px; text-align: center; }
</style>
</head>
<body>
  <main class="sheet">
    <section class="card card--front" aria-label="Card front">
      <div class="brand">
        <span class="brand__square"></span>
        <span class="brand__name">Quartz Hill Lane</span>
      </div>
      <div class="contact">
        <p class="contact__name">Nolan Pryce</p>
        <p class="contact__role">Director</p>
        <ul class="contact__list">
          <li class="contact__item">
            <svg class="contact__icon" viewBox="0 0 16 16" aria-hidden="true"><path d="M4 1l2.5 3.5-1.5 1.8c.8 1.8 2.2 3.2 4 4l1.8-1.5L15 12l-1.6 2.6C7 14.5 1.5 9 1.4 2.6z"/></svg>
            <span>0412 967 154</span>
          </li>
          <li class="contact__item">
            <svg class="contact__icon" viewBox="0 0 16 16" aria-hidden="true"><path d="M4 1l2.5 3.5-1.5 1.8c.8 1.8 2.2 3.2 4 4l1.8-1.5L15 12l-1.6 2.6C7 14.5 1.5 9 1.4 2.6z"/></svg>
            <span>9735 6021</span>
          </li>
          <li class="contact__item">
            <svg class="contact__icon" viewBox="0 0 16 16" aria-hidden="true"><path d="M1 3h14v10H1z M2 4l6 5 6-5" fill="none" stroke="#2b2b2b" stroke-width="1.6"/></svg>
            <span>nolan@quartzhilllane.net.au</span>
          </li>
          <li class="contact__item">
            <span class="contact__label">W</span>
            <span>quartzhilllane.net.au</span>
          </li>
        </ul>
      </div>
    </section>

    <section class="card card--back" aria-label="Card back">
      <div class="brand">
        <span class="brand__square"></span>
        <span class="brand__name">Quartz Hill Lane</span>
      </div>
      <p class="tagline">Property Management</p>
    </section>
  </main>
</body>
</html>
```